Brisk Hollow Builders Needs A Flyer

We need a flyer for our newest product "The Cedarlane Garden Workroom"

Here is some copy for the flyer:

1. More and more people everyday are working from home and finding it difficult to disconnect from home activities in order to focus on their work. They are also finding it very expensive to add on to their existing house for a quiet place. Our archatectually stunning, Cedarlane Garden Workroom is the answer. The office studio measures 16' wide and 10' deep. 160 Square feet of space.

Perfect for dozens of purposes. Home office, design studio, artist studio, home school office, reading room, craft studio, drafting room.

Features include:

- Steel Framing. 40-60% lighter then wood, higher strength to weight ratio, resistant to mold and fire and steel is the most recycled material on earth!
- Spray foam insulation. Cool in the summer and warm in the winter.
- HVAC Mini Split with wireless remote control and thermostat.
- 100% Off grid with enough solar and battery storage to run your entire office. No need to pay for an expensive electric installation.
- Flush fitting floor outlets to reduce wires.
- TV mount (Optional with pre-wired electric, HDMI, digital audio & Cat 6)
- Windows are tempered glass custom made by Morvik Glazing.
- Solar qualifies for a 26% tax credit. This is not a write-off rather it is a direct reduction on your tax obligation.
- Thousands of dollars less than adding onto your home.
- Custom color, siding, features available.

This beautiful back yard office is delivered 100% assembled and ready to enjoy on the day of delivery.

We ship nationwide from our factory in South Carolina. Give us a call anytime to speak to a designer and start your dream office today!

555-318-4027
info@BriskHollowBuilders.example

```html
<!DOCTYPE html>
<html lang="en">
<head>
<meta charset="UTF-8">
<title>Brisk Hollow Builders – The Cedarlane Garden Workroom</title>
<link href="https://fonts.googleapis.com/css2?family=Bebas+Neue&family=Open+Sans:wght@400;600;700&display=swap" rel="stylesheet">
<style>
  :root{
    --page:#e9e9e9;
    --white:#ffffff;
    --forest:#1f3a0c;
    --leaf:#3f9130;
    --gold:#eaa10c;
    --gold-deep:#a87300;
    --ink:#2b2b2b;
    --bar:#2e2e2e;
  }
  *{margin:0;padding:0;box-sizing:border-box}
  html,body{width:720px;height:1200px;overflow:hidden;background:var(--page)}
  .flyer{position:absolute;left:0;top:90px;width:720px;height:1019px;background:var(--white);overflow:hidden;font-family:"Open Sans",sans-serif;color:var(--ink)}
  .flyer-art{position:absolute;left:0;top:0}
  .brand{position:absolute;left:0;top:96px;width:290px;display:flex;align-items:center;justify-content:center;gap:8px}
  .brand-dot{width:14px;height:14px;border-radius:50%;background:var(--leaf)}
  .brand-name{font-family:"Bebas Neue",sans-serif;font-size:27px;letter-spacing:1px;color:var(--forest)}
  .headline{position:absolute;left:43px;top:234px;font-family:"Bebas Neue",sans-serif;line-height:.98}
  .headline .accent{display:block;font-size:56px;color:var(--gold)}
  .headline .sub{display:block;font-size:38px;color:var(--white);margin-top:4px}
  .intro{position:absolute;left:43px;top:454px;width:474px;color:var(--white);font-size:10.4px;font-weight:600;line-height:14.5px}
  .intro p+p{margin-top:5px}
  .features-title{position:absolute;left:42px;top:682px;width:637px;display:flex;align-items:center;gap:18px;font-family:"Bebas Neue",sans-serif;font-size:32px;color:var(--gold)}
  .features-title::before,.features-title::after{content:"";flex:1;height:3px;background:var(--gold)}
  .feature-list{position:absolute;list-style:none;font-size:10.2px;line-height:14px;color:var(--ink)}
  .feature-list.left{left:50px;top:721px;width:300px}
  .feature-list.right{left:399px;top:721px;width:265px}
  .feature-list li{position:relative;padding-left:20px;margin-bottom:5px}
  .feature-list li::before{content:"";position:absolute;left:0;top:0;width:13px;height:13px;border-radius:50%;background:var(--leaf)}
  .feature-list li::after{content:"";position:absolute;left:4px;top:2.5px;width:3px;height:6px;border:solid var(--white);border-width:0 2px 2px 0;transform:rotate(45deg)}
  .delivery-bar{position:absolute;left:42px;top:901px;width:637px;height:34px;background:var(--bar);border-radius:8px 8px 0 0;color:var(--white);font-family:"Bebas Neue",sans-serif;font-size:15px;letter-spacing:.2px;white-space:nowrap;display:flex;align-items:center;justify-content:center}
  .footer{position:absolute;left:0;top:935px;width:720px;height:84px;background:linear-gradient(180deg,var(--gold),var(--gold-deep));color:var(--white);text-align:center}
  .footer-copy{padding-top:8px;font-size:13.4px;line-height:20px}
  .contact{display:flex;justify-content:center;align-items:center;gap:14px;margin-top:5px;font-weight:700;font-size:17px}
  .contact-item{display:flex;align-items:center;gap:6px}
  .contact-icon{width:12px;height:12px;border-radius:50%;background:var(--leaf);display:inline-block}
  .contact-divider{width:2px;height:22px;background:var(--white)}
</style>
</head>
<body>
<main class="flyer">
  <svg class="flyer-art" width="720" height="1019" viewBox="0 0 720 1019">
    <defs>
      <linearGradient id="leafBand" x1="0" y1="0" x2="0" y2="1">
        <stop offset="0" stop-color="#4d9e36"/><stop offset="1" stop-color="#367f27"/>
      </linearGradient>
      <linearGradient id="photoTone" x1="0" y1="0" x2="0" y2="1">
        <stop offset="0" stop-color="#a9c7e0"/><stop offset=".35" stop-color="#6f7478"/><stop offset=".7" stop-color="#3b3d40"/><stop offset="1" stop-color="#5f7f45"/>
      </linearGradient>
      <linearGradient id="smallPhoto" x1="0" y1="0" x2="0" y2="1">
        <stop offset="0" stop-color="#b8d2e6"/><stop offset=".5" stop-color="#4a4c50"/><stop offset="1" stop-color="#5f8a48"/>
      </linearGradient>
      <linearGradient id="thumbTone" x1="0" y1="0" x2="0" y2="1">
        <stop offset="0" stop-color="#2f3033"/><stop offset=".5" stop-color="#cfc8bd"/><stop offset="1" stop-color="#3a3b3e"/>
      </linearGradient>
    </defs>

    <path class="forest-band" d="M0,190 C110,160 250,150 420,152 L420,480 L0,480 Z" fill="var(--forest)"/>
    <path class="leaf-band" d="M0,430 C200,395 430,372 720,362 L720,617 L0,617 Z" fill="url(#leafBand)"/>
    <path class="swoosh" d="M0,430 C200,395 430,372 720,362" fill="none" stroke="var(--white)" stroke-width="5"/>

    <g role="img" aria-label="Photo of the garden workroom with glass doors in a green back yard">
      <path d="M380,0 C318,90 312,300 404,440 C520,400 620,380 720,372 L720,0 Z" fill="url(#photoTone)"/>
    </g>
    <path class="photo-frame" d="M380,0 C318,90 312,300 404,440" fill="none" stroke="var(--gold)" stroke-width="9"/>

    <g role="img" aria-label="Photo of the workroom with solar panels on the roof">
      <circle cx="584" cy="397" r="86" fill="url(#smallPhoto)" stroke="var(--gold)" stroke-width="8"/>
    </g>
    <g role="img" aria-label="Drawing of the steel frame structure">
      <circle cx="587" cy="510" r="66" fill="var(--white)" stroke="var(--gold)" stroke-width="7"/>
    </g>

    <g role="img" aria-label="Workroom exterior view, front left">
      <rect x="68" y="568" width="178" height="108" rx="3" fill="url(#thumbTone)"/>
    </g>
    <g role="img" aria-label="Workroom exterior view, front">
      <rect x="281" y="570" width="172" height="106" rx="3" fill="url(#thumbTone)"/>
    </g>
    <g role="img" aria-label="Workroom exterior view, front right">
      <rect x="474" y="566" width="182" height="110" rx="3" fill="url(#thumbTone)"/>
    </g>
  </svg>

  <div class="brand">
    <span class="brand-dot"></span>
    <span class="brand-name">Brisk Hollow Builders</span>
  </div>

  <h1 class="headline">
    <span class="accent">The Cedarlane</span>
    <span class="accent">Garden</span>
    <span class="sub">Workroom</span>
  </h1>

  <div class="intro">
    <p>More and more people everyday are working from home and finding it difficult to disconnect from home activities in order to focus on their work. They are also finding it very expensive to add on to their existing house for a quiet place. Our archatectually stunning, Cedarlane Garden Workroom is the answer. The office studio measures 16' wide and 10' deep. 160 Square feet of space.</p>
    <p>Perfect for dozens of purposes. Home office, design studio, artist studio, home school office, reading room, craft studio, drafting room.</p>
  </div>

  <h2 class="features-title">Features Include:</h2>

  <ul class="feature-list left">
    <li>Steel Framing. 40-60% lighter then wood, higher strength to weight ratio, resistant to mold and fire and steel is the most recycled material on earth!</li>
    <li>Spray foam insulation. Cool in the summer and warm in the winter.</li>
    <li>HVAC Mini Split with wireless remote control and thermostat.</li>
    <li>Solar qualifies for a 26% tax credit. This is not a write-off rather it is a direct reduction on your tax obligation.</li>
    <li>Custom color, siding, features available.</li>
  </ul>

  <ul class="feature-list right">
    <li>100% Off grid with enough solar and battery storage to run your entire office. No need to pay for an expensive electric installation.</li>
    <li>Flush fitting floor outlets to reduce wires.</li>
    <li>TV mount (Optional with pre-wired electric, HDMI, digital audio &amp; Cat 6)</li>
    <li>Windows are tempered glass custom made by Morvik Glazing.</li>
    <li>Thousands of dollars less than adding onto your home.</li>
  </ul>

  <div class="delivery-bar">This beautiful back yard office is delivered 100% assembled and ready to enjoy on the day of delivery.</div>

  <footer class="footer">
    <p class="footer-copy">We ship nationwide from our factory in South Carolina.<br>Give us a call anytime to speak to a designer and start your dream office today!</p>
    <div class="contact">
      <span class="contact-item"><span class="contact-icon"></span>555-318-4027</span>
      <span class="contact-divider"></span>
      <span class="contact-item"><span class="contact-icon"></span>info@BriskHollowBuilders.example</span>
    </div>
  </footer>
</main>
</body>
</html>
```